Veltrique truck wrap (The most requested fabric protection world wide)

Truck wrap on a 2021 Chey colorado 2 door, What I'm looking for is to engage people with a clean look of what we do! not to busy and easy to read, key points, Logo, Permanent Fabric Protection, Call for free estimate 702 318-5074 #1 choice of Interior Desgners, (maybe a picture of a designer?) Whats the buzz! it is a Rug and furniture fabric protection, Lifetime guarantee! protects form kids and pets, Safe. Colors can be our blue but play with blacks and grays aswell,

Target Market(s)

Truck will be parked at customers home and draw attention to get your rugs and furniture protected

Industry/Entity Type

Rug and Fabric protection, also interior designers

Font styles to use
Sans Serif

Colors

Designer to choose colors to be used in the design.

Requirements
Must have
• Draw attention! uder the wings the tag line( Permanent Fabric Protection)
Nice to have
• Picture of rug or sofa stain, or spill that did not stain!
Should not have
• To much distraction or bussy

```html
<!DOCTYPE html>
<html lang="en">
<head>
<meta charset="utf-8">
<title>Veltrique Truck Wrap – Side Panel Options</title>
<link rel="stylesheet" href="https://fonts.googleapis.com/css2?family=Open+Sans:wght@400;600&family=Roboto+Condensed:wght@500&display=swap">
<style>
  :root {
    --canvas-bg: #eef0f3;
    --wrap-white: #ffffff;
    --wrap-edge: #d9dde3;
    --brand-blue: #2a63ad;
    --brand-blue-light: #4a88cf;
    --brand-blue-deep: #1f4f91;
    --charcoal: #3b3d42;
    --ring-white: #f7f7f7;
    --text-light: #f4f6fa;
    --carpet-light: #ece2cc;
    --carpet-mid: #d2c3a0;
    --stain-warm: #9c6a3a;
    --carpet-grey-light: #d3c9b6;
    --carpet-grey-mid: #b3a386;
    --stain-cool: #8f6b45;
    --cup-white: #f4f5f6;
  }
  * { margin: 0; padding: 0; box-sizing: border-box; }
  html, body { width: 1200px; height: 909px; overflow: hidden; background: var(--canvas-bg); }
  .canvas { position: relative; width: 1200px; height: 909px; }
  .wrap-option { position: absolute; left: 0; width: 1200px; height: 450px; }
  .wrap-option--charcoal { top: 0; }
  .wrap-option--blue { top: 452px; }

  .wrap-panel {
    position: absolute; left: 160px; top: 110px;
    width: 880px; height: 220px;
    background: var(--wrap-white);
    border: 1px solid var(--wrap-edge);
    border-radius: 12px;
    overflow: hidden;
  }
  .wrap-art { position: absolute; inset: 0; }

  .brand-mark {
    position: absolute; left: 52px; top: 92px;
    display: flex; align-items: center; gap: 10px;
    font-family: "Open Sans", sans-serif; font-weight: 600;
    font-size: 30px; line-height: 40px; color: var(--brand-blue); letter-spacing: 0.5px;
  }
  .brand-mark__dot { width: 18px; height: 18px; border-radius: 50%; background: var(--brand-blue); }

  .tagline {
    position: absolute; left: 40px; top: 168px;
    font-family: "Roboto Condensed", sans-serif; font-weight: 500;
    font-size: 18px; line-height: 24px; color: var(--text-light); letter-spacing: 0.4px;
  }
  .call-block {
    position: absolute; left: 566px; top: 38px;
    font-family: "Open Sans", sans-serif; color: var(--text-light);
  }
  .call-block__lead { font-size: 22px; font-weight: 400; line-height: 28px; }
  .call-block__phone { font-size: 33px; font-weight: 400; line-height: 40px; letter-spacing: 0.3px; }
</style>
</head>
<body>
<main class="canvas">

  <section class="wrap-option wrap-option--charcoal">
    <div class="wrap-panel">
      <svg class="wrap-art" width="880" height="220" viewBox="0 0 880 220">
        <defs>
          <radialGradient id="carpetWarm" cx="0.42" cy="0.62" r="0.7">
            <stop offset="0" stop-color="var(--stain-warm)" stop-opacity="0.75"/>
            <stop offset="0.35" stop-color="var(--carpet-mid)"/>
            <stop offset="1" stop-color="var(--carpet-light)"/>
          </radialGradient>
          <linearGradient id="panelSheen" x1="0" y1="0" x2="1" y2="0">
            <stop offset="0" stop-color="var(--brand-blue-deep)"/>
            <stop offset="1" stop-color="var(--brand-blue)"/>
          </linearGradient>
        </defs>
        <polygon class="tagline-band" points="14,162 420,156 420,200 14,200" fill="var(--charcoal)"/>
        <polygon class="call-panel" points="476,22 852,8 852,202 476,202" fill="url(#panelSheen)"/>
        <polygon class="call-panel-map" role="img" aria-label="Dotted world map pattern" points="530,24 852,12 852,196 530,196" fill="var(--brand-blue-light)" opacity="0.22"/>
        <circle class="spill-photo-ring" cx="434" cy="116" r="100" fill="var(--ring-white)"/>
        <circle class="spill-photo" role="img" aria-label="Photo of a tipped coffee cup staining a light carpet" cx="434" cy="116" r="92" fill="url(#carpetWarm)"/>
      </svg>
      <div class="brand-mark"><span class="brand-mark__dot"></span>Veltrique</div>
      <p class="tagline">PERMANENT FABRIC PROTECTION</p>
      <div class="call-block">
        <p class="call-block__lead">Call for free estimate</p>
        <p class="call-block__phone">702 318-5074</p>
      </div>
    </div>
  </section>

  <section class="wrap-option wrap-option--blue">
    <div class="wrap-panel">
      <svg class="wrap-art" width="880" height="220" viewBox="0 0 880 220">
        <defs>
          <radialGradient id="carpetCool" cx="0.45" cy="0.72" r="0.75">
            <stop offset="0" stop-color="var(--stain-cool)" stop-opacity="0.6"/>
            <stop offset="0.4" stop-color="var(--carpet-grey-mid)"/>
            <stop offset="1" stop-color="var(--carpet-grey-light)"/>
          </radialGradient>
          <linearGradient id="panelSheenB" x1="0" y1="0" x2="1" y2="0">
            <stop offset="0" stop-color="var(--brand-blue-deep)"/>
            <stop offset="1" stop-color="var(--brand-blue)"/>
          </linearGradient>
        </defs>
        <polygon class="tagline-band" points="14,162 420,156 420,200 14,200" fill="var(--brand-blue)"/>
        <polygon class="call-panel" points="476,22 852,8 852,202 476,202" fill="url(#panelSheenB)"/>
        <polygon class="call-panel-map" role="img" aria-label="Dotted world map pattern" points="530,24 852,12 852,196 530,196" fill="var(--brand-blue-light)" opacity="0.22"/>
        <circle class="spill-photo-ring" cx="434" cy="116" r="100" fill="var(--ring-white)"/>
        <circle class="spill-photo" role="img" aria-label="Photo of a tipped coffee cup with a spill beading on protected fabric" cx="434" cy="116" r="92" fill="url(#carpetCool)"/>
      </svg>
      <div class="brand-mark"><span class="brand-mark__dot"></span>Veltrique</div>
      <p class="tagline">PERMANENT FABRIC PROTECTION</p>
      <div class="call-block">
        <p class="call-block__lead">Call for free estimate</p>
        <p class="call-block__phone">702 318-5074</p>
      </div>
    </div>
  </section>

</main>
</body>
</html>
```